Corporate Identity Design Project

Teslin Varrow Design is a small boutique event planning and floral design company, based in Northern Alberta. I require the creation of some corporate identity pieces. I want a minimalistic design.
Website www.teslinvarrow.example

Pieces should include
1. Business Card
Should include the company logo, name, email address, address, phone number. These will be professional printed.
These are three cards that I like:
http://cardsamplegallery.example/wp-content/uploads/2010/02/Odile_Vantreck_Roomworks_by_Pepperleaf_studio_Media.jpg
http://neatcardshowcase.example/wp-content/uploads/2011/06/Quiet-Studio-Minimalist-Business-Cards_11.jpg
http://graphicfeedhub.example/wp-content/uploads/2012/03/16.minimalist-business-cards.jpg
I like letterpress, but I am open to other options.

2. Letterhead
will be professionally printed

3. Envelope

4. Fax Sheet
will be printed on home printer

5. Pocket Presentation
Like -http://wrenfieldgardens.example/img/design_step_proposal@2x.jpg

6. Invoice
Like - http://samplehost.example/quillmarsh/2011/02/falcon-athletics-4-letterhead-combined.png?w=529

7. Proposal
Like something like this – this will not be printed, but rather emailed to clients
Like http://files7.imagedepot.example/getfile/files.imagedepot.example/trelvo-studio/nkuBfi2LVj7ENiUb5D16wqAHQHqNNT5vut7mukSTmisfoGHYXGEv9haEQOPL/Picture-52.png.scaled.500.jpg

8. Contract
Like http://www.brightkeyadvertising.example/images/sample-contract.jpg

9. Business Brochure – I have removed this piece from the project and will most likely post it as another project at a later date.

If you think that this is a project of interest to you, but feel that it is “too much” work for the price, please let me know how you would re-package it – I am open to suggestions.

Target Market(s)

Young women

Industry/Entity Type

Boutique

Requirements
Should not have
• I do not want it to look "frilly"

```html
<!DOCTYPE html>
<html lang="en">
<head>
<meta charset="utf-8">
<title>Event Contract – Teslin Varrow Design</title>
<link href="https://fonts.googleapis.com/css2?family=Open+Sans:wght@400;600;700&family=Oswald:wght@500&display=swap" rel="stylesheet">
<style>
  :root {
    --rose: #c1736e;
    --ink: #4a4a4a;
    --rule: #b9b9b9;
    --paper: #ffffff;
  }
  * { box-sizing: border-box; margin: 0; padding: 0; }
  html, body { width: 1200px; height: 528px; overflow: hidden; background: var(--paper); }
  body { position: relative; font-family: "Open Sans", Arial, sans-serif; color: var(--ink); }

  .column { position: absolute; top: 0; height: 528px; }
  .column--left { left: 27px; width: 318px; }
  .column--middle { left: 445px; width: 315px; }
  .column--right { left: 855px; width: 317px; }

  .masthead { position: absolute; top: 6px; left: 60px; width: 260px; height: 52px; }
  .masthead__title { position: absolute; left: 0; top: 27px; font-size: 16.5px; font-weight: 600; color: var(--rose); letter-spacing: 0.1px; white-space: nowrap; }
  .brand { position: absolute; left: 128px; top: 14px; display: flex; align-items: center; gap: 5px; }
  .brand__dot { width: 18px; height: 18px; border-radius: 50%; background: var(--rose); }
  .brand__name { font-size: 9.5px; font-weight: 600; color: var(--rose); line-height: 11px; width: 62px; text-transform: uppercase; letter-spacing: 0.6px; }

  .field { position: absolute; left: 0; right: 0; display: flex; align-items: flex-end; font-size: 9.5px; color: var(--rose); height: 13px; white-space: nowrap; }
  .field__line { flex: 1; border-bottom: 1px solid var(--rule); margin-left: 4px; height: 10px; }
  .field__line--short { flex: 0 0 95px; margin-right: 8px; }

  .copy { position: absolute; left: 0; right: 0; font-size: 7.9px; line-height: 13.5px; text-align: justify; }
  .copy strong { font-weight: 700; }
  .blank { display: inline-block; width: 128px; border-bottom: 1px solid var(--ink); margin: 0 2px; height: 9px; vertical-align: baseline; }

  .tag { display: inline-block; background: var(--rose); color: #fff; font-family: "Oswald", "Arial Narrow", sans-serif; font-weight: 500; font-size: 11.5px; line-height: 14px; padding: 0 4px; margin-right: 6px; letter-spacing: 0.2px; vertical-align: baseline; }

  .contact { position: absolute; left: 0; right: 0; top: 464px; text-align: center; font-size: 7px; letter-spacing: 0.9px; line-height: 13px; color: var(--ink); }
  .contact__row { display: flex; justify-content: center; align-items: center; gap: 6px; letter-spacing: 0.2px; }
  .contact__item { display: flex; align-items: center; gap: 4px; }
  .contact__web { letter-spacing: 1.2px; font-size: 7.5px; }
  .contact__web span { color: var(--rose); }
</style>
</head>
<body>

<section class="column column--left">
  <header class="masthead">
    <h1 class="masthead__title">Event Contract</h1>
    <div class="brand"><span class="brand__dot"></span><span class="brand__name">Teslin Varrow Design</span></div>
  </header>

  <div class="field" style="top:72px">Date Reserved :<span class="field__line"></span></div>
  <div class="field" style="top:95px">Client Name :<span class="field__line"></span></div>
  <div class="field" style="top:119px">Person Financially Responsible :<span class="field__line"></span></div>
  <div class="field" style="top:142px">Mailing Address :<span class="field__line"></span></div>
  <div class="field" style="top:165px">Telephone - Daytime :<span class="field__line field__line--short"></span>Evening :<span class="field__line"></span></div>
  <div class="field" style="top:188px">Email :<span class="field__line"></span></div>
  <div class="field" style="top:211px">Referred by :<span class="field__line"></span></div>
  <div class="field" style="top:234px">Deposit to Hold the Date :<span class="field__line"></span></div>

  <p class="copy" style="top:261px"><strong>I,</strong><span class="blank"></span><strong>(THE CLIENT)</strong> have hired TeslinVarrow Design for my event according to the attached itemized floral proposal. I understand and agree to the following in regard to the flowers I have ordered for my event.</p>

  <p class="copy" style="top:312px">The TeslinVarrow Design reserves the right to cancel this contract if at any time it feels that the obligations cannot be met. TeslinVarrow Design's liability to the client for any claim is limited to a refund to the client for the amount of the fees paid (less the out of pocket wholesale cost for the flowers and supplies and the cost of fuel to and from the event).</p>

  <p class="copy" style="top:389px"><span class="tag">TERMS</span>Payments must be in cash, cheque, or credit card. If a credit card is used, there will be an added surcharge of 1.9% to the order, due to the credit card processing fees. A retainer of $150 is required for confirmation of the event date. <strong>THE CLIENT'S</strong> retainer is <strong>NON-REFUNDABLE</strong>. This contract applies to the floral selections described on the event proposal that is filled out at consultation. The balance is due two weeks prior to the event date. If the event is booked less than 2 weeks prior to date then entire amount is due upon booking. Additions will be accepted up to one week prior to the event date. No guarantee is given that the same flowers will be available on orders made less than two weeks prior to the event. Color and style will match as close as possible.</p>
</section>

<section class="column column--middle">
  <p class="copy" style="top:21px"><span class="tag">CONSULTS</span>The first consultation is free and lasts for one hour. An additional consult at the florist is available for $25 an hour, with a minimum of one hour. Off site inspections are available by appointment for a $50.00 per hour. If <strong>THE CLIENT</strong> needs to come in and talk for any reason and is less than fifteen minutes long, then there is no charge. If items or communication is relayed via email, there are also no fees. If there is any consultation fees accumulated, they will need to be paid for before the flowers are delivered.</p>

  <p class="copy" style="top:120px"><span class="tag">CANCELLATIONS</span><strong>THE CLIENT</strong> understands this is a custom order. <strong>THE CLIENT</strong> also understands if payment is not made in full two weeks prior to the event date, this contract is canceled and all payments are forfeited. Contract cancellation must be made in writing or by email. Contract cancellations made before final payment, will receive a refund of monies paid, less non-refundable retainer. Cancellations made less than 2 weeks prior to the event date will receive <strong>NO refund</strong>.</p>

  <p class="copy" style="top:205px"><span class="tag">SUBSTITUTIONS</span>We reserve the right to make substitutions in the event the flowers received are not of the quality suitable for your event. In this event, the integrity of the proposed color scheme will be maintained and flowers of equivalent value will be used. Example: Wax flowers ordered as a filler flower for bouquets but weather conditions cause unavailability or poor quality. Pink heather or similar filler would be used. Red roses would <strong>NOT</strong> be substituted for white orchids.</p>

  <p class="copy" style="top:291px"><span class="tag">RENTALS</span>All rentals are to be returned 2 days after event or additional rental fees will be charged. If rental items are broken or not returned with in the two days allotted, you will be charged full retail price.</p>

  <p class="copy" style="top:339px"><span class="tag">EXCLUSIVITY</span>It is understood that The TeslinVarrow Design will act as the sole and exclusive florist for your event. By signing this contract <strong>THE CLIENT</strong> agrees that no other person or company, professional or otherwise, shall provide fresh or artificial floral products for <strong>THE CLIENT'S</strong> event location or event reception without the consent of the TeslinVarrow Design. This clause protects the image of The TeslinVarrow Design from assumption that might occur from event attendees. Some exceptions might apply, inquire with the TeslinVarrow Design.</p>

  <p class="copy" style="top:438px"><span class="tag">EVENT GUIDE</span>In the event that <strong>THE CLIENT</strong> will not be available during flower delivery <strong>THE CLIENT</strong> will be responsible for having a designated person meet the florist at the location of drop off. This is to ensure that all items are delivered and accounted for.Once TeslinVarrow Design has delivered the completed floral designs to the agreed upon location(s), it is no longer responsible and will not be held liable for the condition of the flowers.</p>
</section>

<section class="column column--right">
  <p class="copy" style="top:21px">If there is any set up on the part of the TeslinVarrow Design, it is <strong>THE CLIENT'S</strong> responsibility with the event location(s)'s coordinator as to what is acceptable, for example, candles, vases, etc... The person delivering the flowers will <strong>NOT</strong> be held accountable for any damages that may occur if there is not a designated person to sign for and accept delivery. We are not responsible for incorrect delivery times or locations given to us by <strong>THE CLIENT</strong>.</p>

  <p class="copy" style="top:107px">This agreement contains the entire understanding between "The TeslinVarrow Design" and <strong>THE CLIENT</strong>. It supersedes all prior and simultaneous agreements between the parties. The only way to amend this agreement is to do so in writing, and providing the document is signed by all the relevant parties and received within one month of the event date unless otherwise specified.</p>

  <div class="field" style="top:189px">Event Location(s) :<span class="field__line"></span></div>
  <div class="field" style="top:212px">Event Date :<span class="field__line"></span></div>
  <div class="field" style="top:235px">Retainer: $<span class="field__line field__line--short" style="flex-basis:118px"></span>Date Paid :<span class="field__line"></span></div>

  <p class="copy" style="top:266px"><strong>THE CLIENT</strong> understands and agrees to the terms of this contract.</p>

  <div class="field" style="top:291px">Client Signature :<span class="field__line field__line--short"></span>Date :<span class="field__line"></span></div>
  <div class="field" style="top:315px">Client's Printed Name:<span class="field__line"></span></div>

  <footer class="contact">
    <div>P.O. Box 412 | Marrow Creek, Alberta T0A 9Z9</div>
    <div class="contact__row">
      <span class="contact__item">
        <svg width="10" height="10" viewBox="0 0 10 10" aria-hidden="true"><circle cx="5" cy="5" r="5" fill="var(--rose)"/><path d="M3.3 2.6c.3-.3.6-.2.8.1l.5.8c.1.2 0 .4-.1.5l-.3.3c.3.7.8 1.2 1.5 1.5l.3-.3c.1-.1.3-.2.5-.1l.8.5c.3.2.4.5.1.8l-.4.4c-1.6.4-4.4-2.4-4-4z" fill="#fff"/></svg>
        780.555.0142
      </span>
      <span class="contact__item">
        <svg width="10" height="10" viewBox="0 0 10 10" aria-hidden="true"><circle cx="5" cy="5" r="5" fill="var(--rose)"/><rect x="2.3" y="3.2" width="5.4" height="3.8" fill="#fff"/><path d="M2.3 3.2L5 5.3l2.7-2.1" stroke="var(--rose)" stroke-width=".6" fill="none"/></svg>
        hello@teslinvarrow.example
      </span>
    </div>
    <div class="contact__web">www.<span>teslinvarrow</span>.example</div>
  </footer>
</section>

</body>
</html>
```